Corvane Electrical Solutions

On one side. LOGO (underneath:) Commercial Industrial Residential

- NAME & CONTACT DETAILS

Marcus T. Hollings
Project Manager

(Cell icon) (441) 582-6197
(Email icon) cvnelectricalsoultions@mailventra.com
(Facebook & Instagram icons )@cvnelectricalsolutions

Other side: LOGO - underneath ELECTRICAL CONSTRUCTION & MAINTENANCE . LED LIGHTING & AUTOMATION . LIFE SAFETY SYSTEMS (FIRE ALARM / SECURITY) . DATA & COMMUNICATION

```html
<!DOCTYPE html>
<html lang="en">
<head>
<meta charset="utf-8">
<title>Corvane Electrical Solutions — Business Cards</title>
<link rel="stylesheet" href="https://fonts.googleapis.com/css2?family=Lato:wght@400;700&family=Montserrat:wght@500;700&display=swap">
<style>
  :root {
    --backdrop: #d3d3ce;
    --card: #05080a;
    --card-edge: #1d5b78;
    --brand-blue: #1f6688;
    --text-light: #c9cccd;
    --text-muted: #9ea3a6;
  }
  * { box-sizing: border-box; margin: 0; padding: 0; }
  html, body { width: 1200px; height: 801px; overflow: hidden; }
  body {
    background: var(--backdrop);
    font-family: "Lato", sans-serif;
    position: relative;
  }
  .card {
    position: absolute;
    top: 246px;
    width: 540px;
    height: 309px;
    background: var(--card);
    border: 2px solid var(--card-edge);
    border-radius: 3px;
  }
  .card--contact { left: 40px; }
  .card--services { left: 620px; }

  /* brand name lockup */
  .brand {
    display: flex;
    align-items: center;
    gap: 12px;
    font-family: "Montserrat", sans-serif;
    font-weight: 500;
    letter-spacing: 0.14em;
    text-transform: uppercase;
  }
  .brand__mark {
    flex: none;
    background: var(--brand-blue);
  }
  .brand__name { line-height: 1.2; }

  /* contact side */
  .card--contact .brand {
    position: absolute;
    top: 40px;
    left: 0; right: 0;
    justify-content: center;
    color: var(--text-light);
    font-size: 15px;
  }
  .card--contact .brand__mark { width: 14px; height: 14px; }
  .sectors {
    position: absolute;
    top: 92px;
    left: 0; right: 0;
    text-align: center;
    color: var(--brand-blue);
    font-size: 9.5px;
    letter-spacing: 0.12em;
    text-transform: uppercase;
  }
  .sectors span { margin: 0 6px; }
  .person {
    position: absolute;
    left: 34px;
    top: 176px;
  }
  .person__name {
    font-family: "Montserrat", sans-serif;
    font-weight: 700;
    font-size: 23px;
    color: var(--brand-blue);
  }
  .person__role {
    margin-top: 4px;
    font-size: 13px;
    color: var(--text-muted);
    text-align: right;
  }
  .divider {
    position: absolute;
    left: 262px;
    top: 150px;
    width: 1px;
    height: 56px;
    background: var(--card-edge);
  }
  .contacts {
    position: absolute;
    left: 284px;
    top: 142px;
    list-style: none;
    color: var(--text-light);
    font-size: 11.5px;
  }
  .contacts li {
    display: flex;
    align-items: center;
    gap: 8px;
    height: 26px;
  }
  .contacts svg { width: 13px; height: 13px; flex: none; }
  .contacts .social { margin-top: 50px; }

  /* services side */
  .card--services .brand {
    position: absolute;
    top: 52px;
    left: 0; right: 0;
    justify-content: center;
    color: var(--text-light);
    font-size: 21px;
  }
  .card--services .brand__mark { width: 20px; height: 20px; }
  .services {
    position: absolute;
    left: 64px;
    top: 160px;
    list-style: none;
    color: var(--text-light);
    font-size: 12.5px;
    letter-spacing: 0.04em;
    text-transform: uppercase;
  }
  .services li {
    position: relative;
    height: 26px;
    line-height: 26px;
    padding-left: 22px;
  }
  .services li::before {
    content: "";
    position: absolute;
    left: 0;
    top: 10px;
    width: 6px;
    height: 6px;
    border-radius: 50%;
    background: var(--brand-blue);
  }
</style>
</head>
<body>

  <section class="card card--contact" aria-label="Business card, contact side">
    <div class="brand">
      <span class="brand__mark"></span>
      <span class="brand__name">Corvane Electrical Solutions</span>
    </div>
    <p class="sectors">Commercial<span>|</span>Industrial<span>|</span>Residential</p>

    <div class="person">
      <p class="person__name">Marcus T. Hollings</p>
      <p class="person__role">Project Manager</p>
    </div>

    <div class="divider"></div>

    <ul class="contacts">
      <li>
        <svg viewBox="0 0 16 16" aria-hidden="true"><path d="M4 1.5l2.3 3-1.4 1.6c.8 1.8 2.2 3.2 4 4l1.6-1.4 3 2.3-1.3 2.5C6.7 13.5 2.5 9.3 1.5 3.2z" fill="none" stroke="#1f6688" stroke-width="1.6" stroke-linejoin="round"/></svg>
        (441) 582-6197
      </li>
      <li>
        <svg viewBox="0 0 16 16" aria-hidden="true"><rect x="1" y="3" width="14" height="10" fill="#1f6688"/><polyline points="1,3 8,9 15,3" fill="none" stroke="#05080a" stroke-width="1.4"/></svg>
        cvnelectricalsoultions@mailventra.com
      </li>
      <li class="social">
        <svg viewBox="0 0 16 16" aria-hidden="true"><circle cx="8" cy="8" r="7" fill="#1f6688"/></svg>
        @cvnelectricalsolutions
      </li>
    </ul>
  </section>

  <section class="card card--services" aria-label="Business card, services side">
    <div class="brand">
      <span class="brand__mark"></span>
      <span class="brand__name">Corvane Electrical Solutions</span>
    </div>
    <ul class="services">
      <li>Electrical Construction &amp; Maintenance</li>
      <li>LED Lighting &amp; Automation</li>
      <li>Life Safety Systems (Fire Alarm / Security)</li>
      <li>Data &amp; Communication</li>
    </ul>
  </section>

</body>
</html>
```